Stationery Required - Own Logo provided

Hi,

We are a retail company called 'Bramwick Carto Limited' based in the UK and would like some corporate stationery designed.

We have provided our Logo which we would like to use (Its attached to this brief)...

The designs must be orginal, professional, stylish and interesting!

Target Market(s)

We will use this stationery to communicate with our wholesale suppliers and employees, so it must have a 'professional' feel about it.

Industry/Entity Type

It Company

Requirements
Must have
• Must be professional, corporate, stylish and not to 'fussy'. we require ... Business card design, a4 letter, compliment slip. All designs must be supplied in a format where the text (address/telephone numbers etc..) can be edited, as we have alot of staff and operate out of several different premises.
Nice to have
• I would like a windows backround picture file supplied as well so we can integrate that onto our computer systems.

```html
<!DOCTYPE html>
<html lang="en">
<head>
<meta charset="utf-8">
<title>Bramwick Carto Limited – Stationery</title>
<link rel="stylesheet" href="https://fonts.googleapis.com/css2?family=Montserrat:wght@400;600&display=swap">
<style>
  :root {
    --brand-green: #3f7d1f;
    --accent-green: #8cc63f;
    --tint-green: #e3efd3;
    --tint-grey: #c8cdc2;
    --text-grey: #5e5e5e;
    --edge-grey: #8a8a8a;
    --paper: #ffffff;
  }
  * { box-sizing: border-box; margin: 0; padding: 0; }
  html, body { width: 1200px; height: 776px; overflow: hidden; background: var(--paper); }
  body { position: relative; font-family: "Montserrat", Arial, sans-serif; color: var(--text-grey); }

  .sheet { position: absolute; background: var(--paper); border: 1px solid var(--edge-grey); overflow: hidden; }
  .letterhead { left: 114px; top: 9px; width: 524px; height: 737px; }
  .desktop-card { left: 672px; top: 22px; width: 347px; height: 188px; }
  .business-card { left: 672px; top: 247px; width: 347px; height: 214px; }
  .compliment-slip { left: 668px; top: 489px; width: 513px; height: 246px; }

  .brand-pattern { position: absolute; display: block; }
  .letterhead .brand-pattern { left: 0; top: 222px; width: 100%; height: 515px; }
  .compliment-slip .brand-pattern { right: 0; top: 48px; width: 290px; height: 198px; }

  .brand { position: absolute; display: flex; align-items: center; gap: 8px; color: var(--brand-green); font-weight: 600; z-index: 1; }
  .brand-square { background: var(--accent-green); flex: none; }
  .brand-name { line-height: 1; white-space: nowrap; }
  .brand-name .legal { display: block; letter-spacing: 0.45em; margin-top: 3px; }

  .letterhead .brand { left: 24px; top: 18px; font-size: 26px; }
  .letterhead .brand-square { width: 24px; height: 24px; }
  .letterhead .legal { font-size: 9px; }

  .desktop-card .brand { left: 44px; top: 64px; font-size: 26px; }
  .desktop-card .brand-square { width: 26px; height: 26px; }
  .desktop-card .legal { font-size: 9px; }

  .business-card .brand, .compliment-slip .brand { font-size: 19px; gap: 6px; }
  .business-card .brand { left: 16px; top: 22px; }
  .compliment-slip .brand { left: 22px; top: 18px; }
  .business-card .brand-square, .compliment-slip .brand-square { width: 20px; height: 20px; }
  .business-card .legal, .compliment-slip .legal { font-size: 7px; }

  .contact { position: absolute; font-style: normal; z-index: 1; }
  .business-card .contact { right: 22px; top: 76px; text-align: right; font-size: 12.5px; line-height: 18.5px; }
  .contact-name { color: var(--accent-green); font-weight: 600; font-size: 15px; line-height: 20px; }
  .contact-role { color: var(--accent-green); font-size: 14px; line-height: 20px; margin-bottom: 12px; }

  .compliment-slip .contact { left: 248px; top: 18px; font-size: 8px; line-height: 10.5px; color: var(--edge-grey); }
  .slip-caption { position: absolute; right: 18px; bottom: 14px; font-size: 22px; color: var(--text-grey); z-index: 1; }
</style>
</head>
<body>

  <section class="sheet letterhead" aria-label="A4 letterhead">
    <div class="brand">
      <span class="brand-square"></span>
      <span class="brand-name">Bramwick Carto<span class="legal">LIMITED</span></span>
    </div>
    <svg class="brand-pattern" role="img" aria-label="Large faint brand decoration area" viewBox="0 0 524 515" preserveAspectRatio="none">
      <defs>
        <linearGradient id="letterhead-fade" x1="1" y1="0" x2="0" y2="1">
          <stop offset="0" stop-color="#ffffff"/>
          <stop offset="0.35" stop-color="#e3efd3"/>
          <stop offset="1" stop-color="#c8cdc2"/>
        </linearGradient>
      </defs>
      <rect width="524" height="515" fill="url(#letterhead-fade)"/>
    </svg>
  </section>

  <section class="sheet desktop-card" aria-label="Desktop background">
    <div class="brand">
      <span class="brand-square"></span>
      <span class="brand-name">Bramwick Carto<span class="legal">LIMITED</span></span>
    </div>
  </section>

  <section class="sheet business-card" aria-label="Business card">
    <div class="brand">
      <span class="brand-square"></span>
      <span class="brand-name">Bramwick Carto<span class="legal">LIMITED</span></span>
    </div>
    <address class="contact">
      <div class="contact-name">Owen Kearsley</div>
      <div class="contact-role">Company Director</div>
      <div>07700900461</div>
      <div>hello@bramwickcarto.co.uk</div>
      <div>18 Mill Lane, Holbrook</div>
      <div>County Down BT30 9XQ</div>
    </address>
  </section>

  <section class="sheet compliment-slip" aria-label="Compliment slip">
    <svg class="brand-pattern" role="img" aria-label="Faint brand decoration area" viewBox="0 0 290 198" preserveAspectRatio="none">
      <defs>
        <linearGradient id="slip-fade" x1="1" y1="0" x2="0" y2="1">
          <stop offset="0" stop-color="#ffffff"/>
          <stop offset="0.4" stop-color="#e3efd3"/>
          <stop offset="1" stop-color="#c8cdc2"/>
        </linearGradient>
      </defs>
      <rect width="290" height="198" fill="url(#slip-fade)"/>
    </svg>
    <div class="brand">
      <span class="brand-square"></span>
      <span class="brand-name">Bramwick Carto<span class="legal">LIMITED</span></span>
    </div>
    <address class="contact">
      <div>07700900461</div>
      <div>hello@bramwickcarto.co.uk</div>
      <div>18 Mill Lane, Holbrook</div>
      <div>County Down BT30 9XQ</div>
    </address>
    <p class="slip-caption">with compliment slip</p>
  </section>

</body>
</html>
```